Design a PowerPoint template for a consultancy organisation

I am after a Powerpoint template including three pages a title slide (that should have a title and subtitle), A title and content slide and a section header slide. I expect the company name and/or logo to be prominent and the colors to work well with the logo colors. I have included a copy of the logo

```html
<!DOCTYPE html>
<html lang="en">
<head>
<meta charset="utf-8">
<title>Meridian Counsel – Presentation Template</title>
<link href="https://fonts.googleapis.com/css2?family=Poppins:wght@400;500;600;700&family=Open+Sans:wght@400;600&family=Tinos:ital@0;1&display=swap" rel="stylesheet">
<style>
:root{
  --green:#7cc143;
  --purple:#6320b3;
  --ink:#2b2b2b;
  --body:#555;
  --muted:#9a9a9a;
  --stage:#e5e5e5;
  --paper:#ffffff;
  --dark-a:#3d4342;
  --dark-b:#1c1f1f;
}
*{box-sizing:border-box;margin:0;padding:0}
html,body{width:1200px;height:2783px;overflow:hidden;background:var(--stage)}
body{position:relative;font-family:"Open Sans",sans-serif;color:var(--body)}
.slide{position:absolute;width:525px;height:298px;background:var(--paper);overflow:hidden;box-shadow:0 2px 8px rgba(0,0,0,.08)}
.slide-title{position:absolute;left:22px;top:20px;font:600 16px/1 "Poppins",sans-serif;color:var(--ink)}
.slide-sub{position:absolute;left:22px;top:40px;font:600 5.5px/1 "Open Sans",sans-serif;color:#777}
.brand{position:absolute;right:22px;top:16px;display:flex;flex-direction:column;align-items:flex-end;gap:2px}
.brand-dot{width:10px;height:10px;background:var(--purple)}
.brand-name{font:500 10px/1 "Poppins",sans-serif;color:var(--green)}
.footer{position:absolute;left:22px;bottom:10px;font:400 6px/1 "Open Sans",sans-serif;letter-spacing:1px;color:var(--muted)}
.page{position:absolute;right:22px;bottom:10px;font:400 6px/1 "Open Sans",sans-serif;letter-spacing:1px;color:var(--muted)}
.small{font-size:6.2px;line-height:9.5px;color:var(--body)}
.small p{margin-bottom:9px}

/* title slide */
.title-slide{background:var(--dark-b)}
.title-photo{position:absolute;inset:0;background:linear-gradient(120deg,#4a4f4d 0%,var(--dark-a) 40%,#2a2e2d 70%,var(--dark-b) 100%)}
.title-slide .t-brand{position:absolute;left:46px;top:90px;display:flex;align-items:center;gap:4px}
.title-slide .t-brand .brand-dot{width:9px;height:9px}
.title-slide .t-brand .brand-name{font-size:11px}
.t-heading{position:absolute;left:46px;top:128px;font:600 22px/1 "Poppins",sans-serif;color:#fff}
.t-sub{position:absolute;left:46px;top:161px;font:600 6.5px/1 "Poppins",sans-serif;color:#fff}
.t-date{position:absolute;left:46px;bottom:22px;font:600 6.5px/1 "Poppins",sans-serif;color:#fff}
.hero{position:absolute;left:101px;top:240px;width:525px;height:298px;transform:scale(1.9);transform-origin:0 0;box-shadow:0 6px 20px rgba(0,0,0,.2)}

/* toc */
.toc-brand{position:absolute;left:42px;top:107px;display:flex;align-items:center;gap:4px}
.toc-brand .brand-name{font-size:9px}
.toc-brand .brand-dot{width:8px;height:8px}
.toc-heading{position:absolute;left:42px;top:125px;font:500 15px/1 "Poppins",sans-serif;color:var(--ink)}
.toc-list{position:absolute;left:257px;top:28px;width:205px;box-shadow:0 4px 14px rgba(0,0,0,.06);background:#fff;padding:6px 0 10px}
.toc-item{height:32px;display:flex;align-items:center;padding-left:24px;font:400 11px/1 "Poppins",sans-serif;color:var(--ink);border-bottom:1px solid #f0f0f0;position:relative}
.toc-item b{color:var(--green);font-weight:600;margin-right:3px}
.toc-item.active{background:var(--purple);color:#fff;border:none;margin-left:-15px;padding-left:39px;width:205px}
.toc-item.active b{color:#fff}
.toc-item.active::before{content:"";position:absolute;left:10px;border-left:5px solid #fff;border-top:3px solid transparent;border-bottom:3px solid transparent}

.col-head{font:600 11px/1 "Poppins",sans-serif;color:var(--green);margin-bottom:10px}
.col-head.purple{color:var(--purple)}

.stat{position:absolute;top:215px;width:56px;height:47px;color:#fff;text-align:center;padding-top:8px}
.stat strong{display:block;font:600 17px/1 "Poppins",sans-serif}
.stat span{font-size:5px}
.bullets{list-style:disc;padding-left:10px}
.bullets li{margin-bottom:3px}

.member{position:absolute;top:90px;width:110px;text-align:center}
.hex{width:86px;height:96px;margin:0 auto;position:relative}
.member-name{font-size:6.5px;color:#666;margin-top:8px}
.member-role{font-size:5.5px;color:#aaa;font-style:italic;margin-top:4px}

.quote-photo{position:absolute;inset:0;background:linear-gradient(135deg,#f3f4f3 0%,#e6e9e8 45%,#eeeae4 100%)}
.quote-text{position:absolute;left:126px;top:105px;width:250px;font:400 14.5px/19px "Tinos",serif;color:#333}
.quote-text::before{content:"\201C";position:absolute;left:-12px;top:-6px;font-size:28px;color:var(--green)}
.quote-author{position:absolute;left:290px;top:218px;font-size:8px;color:#333;display:flex;align-items:center;gap:10px}
.quote-author i{display:block;width:22px;height:1px;background:#333}

.legend-item{position:absolute;left:345px;font:600 7px/1 "Open Sans",sans-serif;color:var(--ink)}
.legend-item span{display:block;font-weight:400;font-size:5.5px;line-height:9px;color:#666;margin-top:6px}

.steps{position:absolute;left:42px;top:85px;width:442px;height:163px;background:#f5f5f5}
.step{position:absolute;top:0;width:110px;height:100px;background:#fff;padding:10px 20px;font-size:5.5px;line-height:8px;color:#999}
.step h4{font:400 6px/1 "Open Sans",sans-serif;color:#888;margin:14px 0 4px}
.step.on{background:var(--green);color:#eaf6de}
.step.on h4{color:#fff}
.data{position:absolute;top:110px;width:110px;padding:0 20px;font-size:5.5px;line-height:8px;color:#aaa}
.data h5{font:400 6px/1 "Open Sans",sans-serif;color:#888;margin-bottom:3px}
.data em{display:block;margin-top:14px;font-size:4.5px}
</style>
</head>
<body>

<section class="slide title-slide hero" aria-label="Title slide, featured">
  <div class="title-photo" role="img" aria-label="Dimmed photo of a modern office lounge with lamp and chairs"></div>
  <div class="t-brand"><span class="brand-dot"></span><span class="brand-name">Meridian Counsel</span></div>
  <h1 class="t-heading">Presentation Title</h1>
  <p class="t-sub">Sub Presentation Title Goes Here</p>
  <p class="t-date">Date 11 February 2021</p>
</section>

<section class="slide title-slide" style="left:62px;top:1105px">
  <div class="title-photo" role="img" aria-label="Dimmed photo of a modern office lounge with lamp and chairs"></div>
  <div class="t-brand"><span class="brand-dot"></span><span class="brand-name">Meridian Counsel</span></div>
  <h1 class="t-heading">Presentation Title</h1>
  <p class="t-sub">Sub Presentation Title Goes Here</p>
  <p class="t-date">Date 11 February 2021</p>
</section>

<section class="slide title-slide" style="left:620px;top:1105px">
  <div class="title-photo" role="img" aria-label="Dark photo of a modern office lounge with lamp and chairs" style="background:linear-gradient(120deg,#3f4342,#2a2d2c 50%,#141616)"></div>
  <div class="t-brand"><span class="brand-dot"></span><span class="brand-name">Meridian Counsel</span></div>
  <h1 class="t-heading">Presentation Title</h1>
  <p class="t-sub">Sub Presentation Title Goes Here</p>
  <p class="t-date">Date 11 February 2021</p>
</section>

<section class="slide" style="left:62px;top:1438px">
  <h2 class="slide-title">Disclaimer</h2>
  <p class="slide-sub">Sub Heading Text Goes Here</p>
  <div class="brand"><span class="brand-dot"></span><span class="brand-name">Meridian Counsel</span></div>
  <div class="small" style="position:absolute;left:25px;top:80px;width:478px">
    <p>Lorem ipsum dolor sit amet, consectetur adipiscing elit. Integer id nulla magna. Nulla tristique mollis arcu. Vivamus nec dictum turpis. Nulla facilisi. Sed non metus varius, dapibus magna id, elementum ex. Mauris congue pretium tellus, at posuere urna ultrices ut. Cras semper est eget libero dignissim laoreet. Phasellus elementum eget ex et vestibulum. Ut at tellus nulla. Aliquam eleifend consectetur hendrerit. Donec placerat sapien vitae eros fermentum, id venenatis ligula vehicula. Maecenas velit quam, vehicula nec nunc vitae, consequat fringilla nisl.</p>
    <p>Aliquam vitae ligula ut turpis interdum condimentum et ac risus. Nam tellus sapien, scelerisque eu quam vel, egestas auctor ipsum. In aliquam eros vel sapien ultrices, et cursus sapien condimentum. Vestibulum tempus hendrerit est et ultricies. Fusce eu velit fermentum, interdum metus dignissim, aliquam eros. Praesent tempor ipsum quis arcu vestibulum, vel dictum mauris ultrices. Quisque tempor, mi et semper commodo, urna nunc tempor ex, quis suscipit turpis sem sit amet lorem. Duis hendrerit et ex quis finibus. Nullam pretium eu arcu quis dignissim. Phasellus nisl felis, viverra in laoreet ut, laoreet eget orci. Aenean scelerisque velit ac gravida accumsan. Praesent est massa, fermentum nec tincidunt sed, efficitur vel dolor. Ut auctor tincidunt lectus, ut dictum erat.</p>
    <p>In porta magna at erat sodales, quis fringilla sapien lacinia. Pellentesque finibus nisl eget orci facilisis, non ornare leo ullamcorper. Duis quis consectetur felis, vel tincidunt diam. Aenean blandit nisl felis, in rutrum nulla elementum sed. Nam vehicula nibh quis lorem gravida pellentesque. Morbi urna massa, pulvinar sed molestie ac, fermentum ultricies massa. Morbi scelerisque condimentum eros eget convallis. Vestibulum ut libero sed magna tempus volutpat. Duis at dui nibh. Etiam at accumsan nibh. Pellentesque dignissim posuere orci, sollicitudin laoreet eros rutrum gravida.</p>
  </div>
  <p class="footer">© MERIDIAN COUNSEL 2021.ALL RIGHTS</p>
  <p class="page">PAGE 3</p>
</section>

<section class="slide" style="left:620px;top:1438px">
  <div class="toc-brand"><span class="brand-dot"></span><span class="brand-name">Meridian Counsel</span></div>
  <h2 class="toc-heading">Table of Contents</h2>
  <nav class="toc-list">
    <div class="toc-item"><b>01.</b> Disclaimer</div>
    <div class="toc-item"><b>02.</b> Executive Summary</div>
    <div class="toc-item active"><b>03.</b> About Us</div>
    <div class="toc-item"><b>04.</b> Our Team</div>
    <div class="toc-item"><b>05.</b> Portofolio</div>
    <div class="toc-item" style="border:none"><b>06.</b> Infographics &amp; Diagrams</div>
  </nav>
  <p class="footer">© MERIDIAN COUNSEL 2021.ALL RIGHTS</p>
  <p class="page">PAGE 4</p>
</section>

<section class="slide" style="left:62px;top:1771px">
  <h2 class="slide-title">About Us</h2>
  <p class="slide-sub">Sub Heading Text Goes Here</p>
  <div class="brand"><span class="brand-dot"></span><span class="brand-name">Meridian Counsel</span></div>
  <div class="small" style="position:absolute;left:45px;top:86px;width:185px">
    <h3 class="col-head">Heading for this paragraph</h3>
    <p>Lorem Ipsum is simply dummy text of the printing typesetting industry. Lorem Ipsum has been the industry's standard dummy text ever since the 1500s, when an unknown printer took a galley of type and scrambled it to make a type specimen book.</p>
    <p>It has survived not only five centuries, but also the leap into electronic typesetting, remaining essentially unchanged. It was popularised in the 1960s with the release of Letraset sheets containing contrary to popular belief, Lorem Ipsum is not simply random text.</p>
  </div>
  <div class="small" style="position:absolute;left:290px;top:86px;width:185px">
    <h3 class="col-head purple">Heading for this paragraph</h3>
    <p>Lorem Ipsum is simply dummy text of the printing typesetting industry. Lorem Ipsum has been the industry's standard dummy text ever since the 1500s, when an unknown printer took a galley of type and scrambled it to make a type specimen book.</p>
    <p>It has survived not only five centuries, but also the leap into electronic typesetting, remaining essentially unchanged. It was popularised in the 1960s with the release of Letraset sheets containing contrary to popular belief, Lorem Ipsum is not simply random text.</p>
  </div>
  <p class="footer">© MERIDIAN COUNSEL 2021.ALL RIGHTS</p>
  <p class="page">PAGE 5</p>
</section>

<section class="slide" style="left:620px;top:1771px">
  <h2 class="slide-title">Executive Summary</h2>
  <p class="slide-sub">Sub Heading Text Goes Here</p>
  <div class="brand"><span class="brand-dot"></span><span class="brand-name">Meridian Counsel</span></div>
  <div class="small" style="position:absolute;left:40px;top:70px;width:190px;text-align:justify">
    <p>Lorem Ipsum is simply dummy text of the printing typesetting industry. Lorem Ipsum has been the industry's standard dummy text ever since the 1500s, when an unknown printer took a galley of type and scrambled it to make a type specimen book.</p>
    <p>It has survived not only five centuries, but also the leap into electronic typesetting, remaining essentially unchanged. It was popularised in the 1960s with the release of Letraset sheets containing contrary to popular belief, Lorem Ipsum is not simply random text.</p>
  </div>
  <div class="stat" style="left:38px;background:var(--green)"><strong>291</strong><span>Custom Text</span></div>
  <div class="stat" style="left:102px;background:var(--purple)"><strong>21</strong><span>Custom Text</span></div>
  <div class="stat" style="left:166px;background:var(--green)"><strong>758</strong><span>Custom Text</span></div>
  <div class="small" style="position:absolute;left:275px;top:78px;width:200px">
    <h3 class="col-head purple">Bullet with Information Text</h3>
    <ul class="bullets">
      <li>Lorem Ipsum is simply dummy text of the printing typesetting industry.</li>
      <li>Lorem Ipsum has been the industry's standard dummy text ever since the 1500s, when an unknown printer took a galley of type and scrambled it to make a type specimen book.</li>
      <li>It has survived not only five centuries, but also the leap into electronic typesetting, remaining essentially unchanged.</li>
      <li>It was popularised in the 1960s with the release of Letraset sheets containing contrary to popular belief, Lorem Ipsum is not simply random text.</li>
    </ul>
  </div>
  <p class="footer">© MERIDIAN COUNSEL 2021.ALL RIGHTS</p>
  <p class="page">PAGE 6</p>
</section>

<section class="slide" style="left:62px;top:2103px">
  <h2 class="slide-title">Our Team</h2>
  <p class="slide-sub">Sub Heading Text Goes Here</p>
  <div class="brand"><span class="brand-dot"></span><span class="brand-name">Meridian Counsel</span></div>
  <div class="member" style="left:53px">
    <svg class="hex" viewBox="0 0 86 96" role="img" aria-label="Portrait photo of team member"><polygon points="43,0 86,24 86,72 43,96 0,72 0,24" fill="#dfe6ea"/><circle cx="66" cy="78" r="9" fill="var(--green)"/><circle cx="66" cy="75.5" r="2.3" fill="#fff"/><path d="M62 82a4 4 0 0 1 8 0z" fill="#fff"/></svg>
    <p class="member-name">Daniel R. Moore</p><p class="member-role">CEO, Founder</p>
  </div>
  <div class="member" style="left:208px">
    <svg class="hex" viewBox="0 0 86 96" role="img" aria-label="Portrait photo of team member"><polygon points="43,0 86,24 86,72 43,96 0,72 0,24" fill="#efdcd6"/><circle cx="66" cy="78" r="9" fill="var(--purple)"/><path d="M62 82l1-3 5-5 2 2-5 5z" fill="#fff"/></svg>
    <p class="member-name">Clara J. Winslow</p><p class="member-role">Content Writer</p>
  </div>
  <div class="member" style="left:353px">
    <svg class="hex" viewBox="0 0 86 96" role="img" aria-label="Portrait photo of team member"><polygon points="43,0 86,24 86,72 43,96 0,72 0,24" fill="#dde6df"/><circle cx="66" cy="78" r="9" fill="var(--green)"/><circle cx="65" cy="77" r="3" fill="none" stroke="#fff" stroke-width="1.3"/><path d="M67 79l3 3" stroke="#fff" stroke-width="1.3"/></svg>
    <p class="member-name">Owen T. Hale</p><p class="member-role">Senior Graphic Designer</p>
  </div>
  <p class="footer">MERIDIAN COUNSEL 2021.ALL RIGHTS</p>
  <p class="page">PAGE 7</p>
</section>

<section class="slide" style="left:620px;top:2103px">
  <div class="quote-photo" role="img" aria-label="Faded photo of an office lounge with lamp and sofa"></div>
  <blockquote class="quote-text">Stress and worry, they solve nothing. What they do is block creativity. You are not even able to think about the solutions. Every problem has a solution.</blockquote>
  <p class="quote-author"><i></i>Maya K. Ortiz</p>
</section>

<section class="slide" style="left:62px;top:2436px">
  <h2 class="slide-title">Infographic &amp; Charts</h2>
  <p class="slide-sub">Sub Heading Text Goes Here</p>
  <div class="brand"><span class="brand-dot"></span><span class="brand-name">Meridian Counsel</span></div>
  <svg style="position:absolute;left:30px;top:80px" width="260" height="160" viewBox="0 0 260 160" font-family="Open Sans, sans-serif" font-size="5.5" fill="#555">
    <g stroke="#eee" stroke-width="0.7">
      <line x1="20" y1="10" x2="250" y2="10"/><line x1="20" y1="31" x2="250" y2="31"/><line x1="20" y1="52" x2="250" y2="52"/><line x1="20" y1="73" x2="250" y2="73"/><line x1="20" y1="94" x2="250" y2="94"/><line x1="20" y1="115" x2="250" y2="115"/>
    </g>
    <line x1="20" y1="136" x2="250" y2="136" stroke="#ccc" stroke-width="0.7"/>
    <g text-anchor="end"><text x="14" y="12">6</text><text x="14" y="33">5</text><text x="14" y="54">4</text><text x="14" y="75">3</text><text x="14" y="96">2</text><text x="14" y="117">1</text><text x="14" y="138">0</text></g>
    <g>
      <rect x="34" y="46" width="10" height="90" fill="var(--green)"/><rect x="45" y="86" width="10" height="50" fill="var(--purple)"/><rect x="56" y="94" width="10" height="42" fill="#a5a5a5"/>
      <rect x="92" y="84" width="10" height="52" fill="var(--green)"/><rect x="103" y="44" width="10" height="92" fill="var(--purple)"/><rect x="114" y="94" width="10" height="42" fill="#a5a5a5"/>
      <rect x="150" y="63" width="10" height="73" fill="var(--green)"/><rect x="161" y="98" width="10" height="38" fill="var(--purple)"/><rect x="172" y="73" width="10" height="63" fill="#a5a5a5"/>
      <rect x="208" y="42" width="10" height="94" fill="var(--green)"/><rect x="219" y="77" width="10" height="59" fill="var(--purple)"/><rect x="230" y="31" width="10" height="105" fill="#a5a5a5"/>
    </g>
    <g text-anchor="middle"><text x="50" y="147">Category 1</text><text x="108" y="147">Category 2</text><text x="166" y="147">Category 3</text><text x="224" y="147">Category 4</text></g>
    <rect x="90" y="153" width="4" height="4" fill="var(--green)"/><text x="96" y="157">Series 1</text>
    <rect x="122" y="153" width="4" height="4" fill="var(--purple)"/><text x="128" y="157">Series 2</text>
    <rect x="154" y="153" width="4" height="4" fill="#a5a5a5"/><text x="160" y="157">Series 3</text>
  </svg>
  <svg style="position:absolute;left:317px;top:82px" width="20" height="130" viewBox="0 0 20 130" fill="none" stroke="#444" stroke-width="1">
    <circle cx="8" cy="6" r="4"/><path d="M1 18c1-6 13-6 14 0"/>
    <path d="M2 61a8 7 0 1 1 3 5l-4 2z"/><circle cx="6" cy="60" r=".7" fill="#444"/><circle cx="10" cy="60" r=".7" fill="#444"/><circle cx="14" cy="60" r=".7" fill="#444"/>
    <path d="M3 110l7-7 7 7-7 7z"/><path d="M6 107l4 4"/>
  </svg>
  <p class="legend-item" style="top:84px">Device Chart<span>Lorem ipsum dolor amet cons<br>adipiscing elit eiusmo temp</span></p>
  <p class="legend-item" style="top:141px">Device Chart<span>Lorem ipsum dolor amet cons<br>adipiscing elit eiusmo temp</span></p>
  <p class="legend-item" style="top:198px">Device Chart<span>Lorem ipsum dolor amet cons<br>adipiscing elit eiusmo temp</span></p>
  <p class="footer">© MERIDIAN COUNSEL 2021.ALL RIGHTS</p>
  <p class="page">PAGE 9</p>
</section>

<section class="slide" style="left:620px;top:2436px">
  <h2 class="slide-title">Infographic &amp; Charts</h2>
  <p class="slide-sub">Sub Heading Text Goes Here</p>
  <div class="brand"><span class="brand-dot"></span><span class="brand-name">Meridian Counsel</span></div>
  <div class="steps">
    <div class="step" style="left:0"><svg width="8" height="8" viewBox="0 0 8 8"><circle cx="4" cy="4" r="3.5" fill="none" stroke="#bbb"/><path d="M4 4V.5A3.5 3.5 0 0 1 7.5 4z" fill="#bbb"/></svg><h4>Step 01</h4>A wonderful serenity has taken possession of my entire soul, like these sweet mornings spring.</div>
    <div class="step on" style="left:110px"><svg width="8" height="8" viewBox="0 0 8 8"><circle cx="4" cy="4" r="2.5" fill="none" stroke="#fff" stroke-width="1.4" stroke-dasharray="1.5 .8"/></svg><h4>Step 02</h4>A wonderful serenity has taken possession of my entire soul, like these sweet mornings spring.</div>
    <svg style="position:absolute;left:220px;top:38px" width="10" height="24" viewBox="0 0 10 24"><path d="M0 0l10 12L0 24z" fill="var(--green)"/></svg>
    <div class="step" style="left:221px"><svg width="8" height="8" viewBox="0 0 8 8" fill="none" stroke="#bbb"><path d="M2 1h4v2a2 2 0 0 1-4 0zM4 5v2M2.5 7.5h3"/></svg><h4>Step 03</h4>A wonderful serenity has taken possession of my entire soul, like these sweet mornings spring.</div>
    <div class="step" style="left:332px"><svg width="8" height="8" viewBox="0 0 8 8"><path d="M7 1L3 3 1 6l2-1 1 2 1-3z" fill="#bbb"/></svg><h4>Step 04</h4>A wonderful serenity has taken possession of my entire soul, like these sweet mornings spring.</div>
    <div class="data" style="left:0"><h5>25% Data</h5>A wonderful serenity has taken possession<em>March 24, 2018</em></div>
    <div class="data" style="left:110px"><h5 style="color:var(--green)">50% Data</h5>A wonderful serenity has taken possession<em>March 28, 2018</em></div>
    <div class="data" style="left:221px"><h5>75% Data</h5>A wonderful serenity has taken possession<em>April 07, 2018</em></div>
    <div class="data" style="left:332px"><h5>100% Data</h5>A wonderful serenity has taken possession<em>April 15, 2018</em></div>
  </div>
  <p class="footer">MERIDIAN COUNSEL 2021.ALL RIGHTS</p>
  <p class="page">PAGE 10</p>
</section>

</body>
</html>
```